Business Card and Stationery for Brokerage & Consulting Co.
Amber Ridge Associates, Brokerage & Consulting for the Baking Industry
Business Card and Stationery for Brokerage & Consulting Co. - Food
Creative Brief
Professional
Derek Halvorsen
Partner / Business Development
4219 W. Birchmont Ave. Long Beach, CA 90714
derek@amberridgeassociates.com

```html
<!DOCTYPE html>
<html lang="en">
<head>
<meta charset="utf-8">
<title>Amber Ridge Associates — Stationery</title>
<link rel="stylesheet" href="https://fonts.googleapis.com/css2?family=Lato:wght@400;700&display=swap">
<style>
  :root {
    --plum: #4a2430;
    --rose: #b88a96;
    --olive: #6b7a45;
    --paper: #ffffff;
    --paper-shade: #f3f1ee;
    --ink: #5a4a4e;
    --backdrop: #e6ddd1;
    --tree-tone: #d9d4d2;
    --crease: #ddd8d3;
  }
  * { box-sizing: border-box; margin: 0; padding: 0; }
  html, body { width: 1200px; height: 446px; overflow: hidden; }
  body {
    position: relative;
    background: var(--backdrop);
    font-family: "Lato", sans-serif;
    color: var(--ink);
  }
  .sheet {
    position: absolute;
    background: var(--paper);
    box-shadow: 0 2px 6px rgba(60, 40, 30, .25);
  }
  .brand {
    display: flex;
    align-items: center;
    gap: 4px;
    font-family: "Lato", sans-serif;
    font-weight: 700;
    color: var(--plum);
    white-space: nowrap;
  }
  .brand-dot { border-radius: 50%; background: var(--plum); flex: none; }

  /* Business cards */
  .card-front { left: 19px; top: 156px; width: 125px; height: 62px; }
  .card-front .brand { position: absolute; left: 8px; top: 7px; font-size: 6.5px; }
  .card-front .brand-dot { width: 9px; height: 9px; }
  .card-front .card-details {
    position: absolute; left: 21px; top: 20px;
    font-size: 3.6px; line-height: 1.55; white-space: nowrap;
  }
  .card-front .card-band { position: absolute; left: 0; right: 0; bottom: 10px; height: 5px; background: var(--plum); }
  .card-back { left: 19px; top: 252px; width: 125px; height: 62px; display: flex; align-items: center; justify-content: center; }
  .card-back .brand { font-size: 8px; }
  .card-back .brand-dot { width: 11px; height: 11px; }

  /* Letterheads */
  .letterhead { top: 12px; width: 288px; height: 412px; }
  .letterhead-one { left: 168px; }
  .letterhead-two { left: 475px; }
  .letterhead .brand { position: absolute; font-size: 8px; }
  .letterhead .brand-dot { width: 12px; height: 12px; }
  .letterhead-one .brand { left: 26px; top: 16px; }
  .letterhead-two .brand { left: 50%; top: 16px; transform: translateX(-50%); }
  .letterhead .contact { position: absolute; right: 24px; top: 14px; font-size: 4.2px; line-height: 1.6; }
  .tree-backdrop {
    position: absolute;
    border-radius: 48% 52% 40% 40%;
    background: radial-gradient(ellipse at 50% 40%, var(--tree-tone) 0%, rgba(217,212,210,.5) 55%, rgba(217,212,210,0) 75%);
  }
  .letterhead-one .tree-backdrop { left: 40px; top: 230px; width: 150px; height: 180px; }
  .letterhead-two .tree-backdrop { left: 70px; top: 130px; width: 150px; height: 180px; }
  .footer-band { position: absolute; left: 0; right: 0; bottom: 22px; height: 9px; background: var(--plum); }
  .footer-rule { position: absolute; left: 0; right: 0; bottom: 18px; height: 2px; background: var(--rose); }
  .footer-text { position: absolute; left: 0; right: 0; bottom: 6px; font-size: 4.2px; text-align: center; }

  /* Envelopes */
  .envelope { left: 792px; width: 396px; height: 96px; overflow: hidden; }
  .envelope svg { position: absolute; inset: 0; }
  .envelope-plum { top: -10px; }
  .envelope-olive { top: 82px; }
  .envelope-open { top: 180px; }
  .envelope-open .brand { position: absolute; left: 50%; top: 52px; transform: translateX(-50%); font-size: 7px; }
  .envelope-open .brand-dot { width: 11px; height: 11px; }
  .envelope-front { left: 792px; top: 300px; width: 396px; height: 112px; }
  .envelope-front .brand { position: absolute; left: 16px; top: 14px; font-size: 7px; }
  .envelope-front .brand-dot { width: 11px; height: 11px; }
  .envelope-front .return-address { position: absolute; left: 16px; top: 32px; font-size: 4px; line-height: 1.6; }
  .envelope-front .footer-band { bottom: 14px; height: 6px; }
  .envelope-front .footer-rule { bottom: 10px; }
</style>
</head>
<body>

  <section class="sheet card-front" aria-label="Business card front">
    <div class="brand"><span class="brand-dot"></span>Amber Ridge Associates</div>
    <div class="card-details">Derek Halvorsen<br>Partner / Business Development<br>derek@amberridgeassociates.com</div>
    <div class="card-band"></div>
  </section>

  <section class="sheet card-back" aria-label="Business card back">
    <div class="brand"><span class="brand-dot"></span>Amber Ridge Associates</div>
  </section>

  <section class="sheet letterhead letterhead-one" aria-label="Letterhead option one">
    <div class="brand"><span class="brand-dot"></span>Amber Ridge Associates</div>
    <div class="contact">4219 W. Birchmont Ave.<br>Long Beach, CA 90714<br>derek@amberridgeassociates.com</div>
    <div class="tree-backdrop" role="img" aria-label="Faint tree illustration"></div>
  </section>

  <section class="sheet letterhead letterhead-two" aria-label="Letterhead option two">
    <div class="brand"><span class="brand-dot"></span>Amber Ridge Associates</div>
    <div class="tree-backdrop" role="img" aria-label="Faint tree illustration"></div>
    <div class="footer-band"></div>
    <div class="footer-rule"></div>
    <div class="footer-text">4219 W. Birchmont Ave. Long Beach, CA 90714 · derek@amberridgeassociates.com</div>
  </section>

  <section class="sheet envelope envelope-plum" aria-label="Envelope back, plum liner">
    <svg width="396" height="96" viewBox="0 0 396 96">
      <rect width="396" height="96" fill="var(--paper-shade)"/>
      <path d="M0 0 H396 V20 L198 92 L0 20 Z" fill="var(--plum)"/>
    </svg>
  </section>

  <section class="sheet envelope envelope-olive" aria-label="Envelope back, olive liner">
    <svg width="396" height="96" viewBox="0 0 396 96">
      <rect width="396" height="96" fill="var(--paper-shade)"/>
      <path d="M0 0 H396 V20 L198 60 L0 20 Z" fill="var(--olive)"/>
      <path d="M0 96 L198 60 L396 96" fill="none" stroke="var(--crease)" stroke-width="1"/>
    </svg>
  </section>

  <section class="sheet envelope envelope-open" aria-label="Envelope back, white flap">
    <svg width="396" height="96" viewBox="0 0 396 96">
      <rect width="396" height="96" fill="var(--paper-shade)"/>
      <path d="M0 0 H396 V14 L198 48 L0 14 Z" fill="var(--paper)" stroke="var(--crease)"/>
    </svg>
    <div class="brand"><span class="brand-dot"></span>Amber Ridge Associates</div>
  </section>

  <section class="sheet envelope-front" aria-label="Envelope front">
    <div class="brand"><span class="brand-dot"></span>Amber Ridge Associates</div>
    <div class="return-address">4219 W. Birchmont Ave.<br>Long Beach, CA 90714</div>
    <div class="footer-band"></div>
    <div class="footer-rule"></div>
  </section>

</body>
</html>
```